business card Quintavo

Wee need a business card design for a new compagny based on Paris
We developped innovative a platform for selling services to refresh, beautify and develop its housing.
We would like a red logo on a black background
Te final design should communicate quality service, know-how, high-end

Target Market(s)

individuals

Industry/Entity Type

Business

```html
<!DOCTYPE html>
<html lang="en">
<head>
<meta charset="utf-8">
<title>Quintavo business card</title>
<link rel="stylesheet" href="https://fonts.googleapis.com/css2?family=Questrial&family=Arimo&family=Open+Sans&display=swap">
<style>
  :root {
    --canvas-grey: #6b6b6b;
    --card-white: #ffffff;
    --card-black: #000000;
    --brand-coral: #f25c68;
    --wordmark-grey: #8a8a8a;
    --text-dark: #3a3a3a;
    --text-mid: #555555;
  }
  html, body {
    margin: 0;
    padding: 0;
    width: 1035px;
    height: 1200px;
    overflow: hidden;
    background: var(--canvas-grey);
  }
  .canvas {
    position: relative;
    width: 1035px;
    height: 1200px;
  }
  .card {
    position: absolute;
    left: 136px;
    width: 762px;
    height: 436px;
    overflow: hidden;
  }
  .card--front {
    top: 131px;
    background: var(--card-white);
  }
  .card--back {
    top: 631px;
    background: var(--card-black);
  }
  .front-band {
    position: absolute;
    left: 0;
    bottom: 0;
    width: 100%;
    height: 30px;
    background: var(--card-black);
  }
  .holder {
    position: absolute;
    left: 69px;
    top: 63px;
    font-family: "Open Sans", sans-serif;
    font-size: 16px;
    line-height: 23px;
    color: var(--text-mid);
  }
  .holder__role {
    font-size: 14px;
  }
  .brand {
    position: absolute;
    display: flex;
    align-items: center;
  }
  .brand--front { left: 69px; top: 198px; }
  .brand--back { left: 210px; top: 182px; }
  .brand__square {
    width: 75px;
    height: 75px;
    background: var(--brand-coral);
    flex: none;
  }
  .brand__name {
    margin-left: 17px;
    font-family: "Questrial", sans-serif;
    font-size: 62px;
    line-height: 1;
    color: var(--wordmark-grey);
    letter-spacing: -0.5px;
  }
  .contact {
    position: absolute;
    left: 512px;
    top: 126px;
    font-family: "Arimo", sans-serif;
    font-size: 19px;
    line-height: 23.5px;
    color: var(--text-dark);
  }
  .contact p {
    margin: 0 0 23.5px 0;
  }
</style>
</head>
<body>
<main class="canvas">
  <section class="card card--front">
    <div class="holder">
      <div class="holder__name">Name xxxxxxxxxxxxx</div>
      <div class="holder__role">xxxxxxxxxxxxxxxxxx</div>
    </div>
    <div class="brand brand--front">
      <div class="brand__square"></div>
      <div class="brand__name">Quintavo</div>
    </div>
    <div class="contact">
      <p>0000 Linden Road<br>Suite #0000<br>Maple Hollow<br>ZT 00000</p>
      <p>Phone: 000-000-0001<br>Fax: 000-000-0000</p>
      <p>info@quintavo.fr<br>www.quintavo.fr</p>
    </div>
    <div class="front-band"></div>
  </section>
  <section class="card card--back">
    <div class="brand brand--back">
      <div class="brand__square"></div>
      <div class="brand__name">Quintavo</div>
    </div>
  </section>
</main>
</body>
</html>
```